New Business Card Design Project

Target Market(s)

Passing cards out

Industry/Entity Type

Asphalt contractor

Contact Information for Business Card

Crestwick Paving

Colors
FFC000
F8CF3A
FAE287
FDF2CF
FEFAEE
F0912C
F2A743
F7CA91
FBE8D2
FDF5EE
EE7325
F08F49
F5BC92
FAE3D3
FDF4ED

Requirements
Must have
• Asphalt
Nice to have
• Would like to have 2 pictures on it of equipment

```html
<!DOCTYPE html>
<html lang="en">
<head>
<meta charset="UTF-8">
<title>Crestwick Paving – Business Card</title>
<link href="https://fonts.googleapis.com/css2?family=Archivo+Black&family=Montserrat:wght@400;500;600;700&display=swap" rel="stylesheet">
<style>
  :root{
    --backdrop:#e4d198;
    --card-yellow:#ffe500;
    --card-white:#ffffff;
    --ink:#111111;
    --ink-soft:#2d2d2d;
    --brand-red:#d8120f;
    --accent-orange:#f0912c;
    --rock-dark:#2a2a2a;
    --rock-mid:#6b6b6b;
  }
  *{box-sizing:border-box;margin:0;padding:0}
  html,body{width:697px;height:1200px;overflow:hidden}
  body{
    background:var(--backdrop);
    display:flex;flex-direction:column;align-items:center;justify-content:center;gap:40px;
    font-family:"Montserrat",sans-serif;color:var(--ink);
  }
  .card{
    position:relative;width:503px;height:287px;overflow:hidden;
    box-shadow:0 14px 16px -10px rgba(0,0,0,.35);
  }
  /* front */
  .card--front{background:var(--card-white);padding:7px}
  .front-face{position:relative;width:100%;height:100%;background:var(--card-yellow)}
  .rock-cluster{position:absolute;border-radius:50%}
  .rock-cluster--left{left:-10px;top:-10px;width:100px;height:105px;
    background:radial-gradient(circle at 40% 40%,var(--rock-mid),var(--rock-dark) 45%,rgba(42,42,42,0) 72%)}
  .rock-cluster--right{right:-12px;top:20px;width:80px;height:100px;
    background:radial-gradient(circle at 55% 50%,var(--rock-mid),var(--rock-dark) 45%,rgba(42,42,42,0) 72%)}
  .brand-name{
    position:absolute;left:0;right:0;top:36px;text-align:center;
    font-family:"Archivo Black",sans-serif;color:var(--brand-red);
    font-size:33px;line-height:1.05;letter-spacing:-.5px;
  }
  .brand-name small{display:block;font-size:17px;letter-spacing:3px}
  .headline{
    position:absolute;left:0;right:0;top:142px;text-align:center;
    font-family:"Archivo Black",sans-serif;font-size:17px;letter-spacing:-.6px;
  }
  .services{
    position:absolute;left:38px;top:174px;
    display:grid;grid-template-columns:146px 150px 120px;row-gap:5px;
    list-style:none;font-size:15px;color:var(--ink-soft);
  }
  .services li{display:flex;align-items:center;gap:7px;white-space:nowrap}
  .services svg{width:12px;height:12px;flex:none}
  .phones{
    position:absolute;left:0;right:0;top:237px;display:flex;justify-content:center;gap:26px;
    font-weight:700;font-size:16.5px;
  }
  .phones span{display:flex;align-items:center;gap:8px}
  .phones svg{width:12px;height:12px}
  /* back */
  .card--back{background:var(--card-white)}
  .partner-names{
    position:absolute;left:0;right:0;top:28px;text-align:center;
    font-family:"Archivo Black",sans-serif;color:var(--brand-red);font-size:28px;line-height:1.15;letter-spacing:-.8px;
  }
  .equipment-photo{position:absolute}
  .equipment-photo--left{left:0;top:83px;width:155px;height:145px;
    background:linear-gradient(160deg,#2b2b2b 0 25%,#b52a24 25% 60%,#3a3a3a 60%);border-radius:6px 20px 10px 6px}
  .equipment-photo--right{left:346px;top:94px;width:157px;height:142px;
    background:linear-gradient(160deg,#3b3b3b 0 22%,#8d8a86 22% 55%,#e0a21e 55% 80%,#444 80%);border-radius:20px 6px 6px 10px}
  .tagline{position:absolute;left:0;right:0;top:142px;text-align:center;color:var(--ink-soft)}
  .tagline .line-one{display:block;font-size:19px;font-weight:500}
  .tagline .line-two{display:block;font-size:27px;font-weight:600;line-height:1.05}
  .email{
    position:absolute;left:0;right:0;top:253px;display:flex;justify-content:center;align-items:center;gap:10px;
    font-size:15px;font-weight:500;color:var(--ink-soft);
  }
  .email svg{width:16px;height:12px}
</style>
</head>
<body>
  <section class="card card--front" aria-label="Business card front">
    <div class="front-face">
      <div class="rock-cluster rock-cluster--left" role="img" aria-label="Scattered asphalt chunks"></div>
      <div class="rock-cluster rock-cluster--right" role="img" aria-label="Scattered asphalt chunks"></div>
      <h1 class="brand-name">CRESTWICK<small>PAVING</small></h1>
      <h2 class="headline">SPEACIALIST IN CHIPSEAL &amp; HOTMIX</h2>
      <ul class="services">
        <li><svg viewBox="0 0 12 12"><path d="M1 6.5l3.2 3.2L11 2" fill="none" stroke="#111" stroke-width="2"/></svg>Ranch Roads</li>
        <li><svg viewBox="0 0 12 12"><path d="M1 6.5l3.2 3.2L11 2" fill="none" stroke="#111" stroke-width="2"/></svg>Sub Divisions</li>
        <li><svg viewBox="0 0 12 12"><path d="M1 6.5l3.2 3.2L11 2" fill="none" stroke="#111" stroke-width="2"/></svg>Driveways</li>
        <li><svg viewBox="0 0 12 12"><path d="M1 6.5l3.2 3.2L11 2" fill="none" stroke="#111" stroke-width="2"/></svg>City Streets</li>
        <li><svg viewBox="0 0 12 12"><path d="M1 6.5l3.2 3.2L11 2" fill="none" stroke="#111" stroke-width="2"/></svg>Patching</li>
        <li><svg viewBox="0 0 12 12"><path d="M1 6.5l3.2 3.2L11 2" fill="none" stroke="#111" stroke-width="2"/></svg>Parking Lots</li>
      </ul>
      <div class="phones">
        <span><svg viewBox="0 0 12 12"><path d="M2.5 1l2 2.3-1 1.3a7 7 0 003.9 3.9l1.3-1 2.3 2-1.3 1.5C5.5 11 1 6.5.9 2.3z" fill="#d8120f"/></svg>555 014 2270</span>
        <span><svg viewBox="0 0 12 12"><path d="M2.5 1l2 2.3-1 1.3a7 7 0 003.9 3.9l1.3-1 2.3 2-1.3 1.5C5.5 11 1 6.5.9 2.3z" fill="#d8120f"/></svg>555 018 4391</span>
      </div>
    </div>
  </section>

  <section class="card card--back" aria-label="Business card back">
    <h2 class="partner-names">WADE CARTER<br>COLT CARTER</h2>
    <div class="equipment-photo equipment-photo--left" role="img" aria-label="Red dump truck loaded with asphalt"></div>
    <div class="equipment-photo equipment-photo--right" role="img" aria-label="Yellow dump truck loaded with asphalt"></div>
    <p class="tagline"><span class="line-one">DO IT RIGHT</span><span class="line-two">SINCE 1992</span></p>
    <p class="email"><svg viewBox="0 0 16 12"><rect width="16" height="12" rx="1.5" fill="#f0912c"/><path d="M1 1.5l7 5 7-5" fill="none" stroke="#fff" stroke-width="1.4"/></svg>crestwickpaving@mail.com</p>
  </section>
</body>
</html>
```